Velmorique needs a elegant mystical business card design

The theme of Velmorique is centered on Kemetic/Ancient Egyptian Spirituality. My business sells handmade scented candles, mystic oils, body sprays, tarot readings and more. I would like my business card to reflect an elegant and mystical look. Hieroglyphs around the borders would be a cool idea. Also, the main colors I am working with is Black and Gold= colors of royalty. Black background. The business card will be double sided. The back will have the logo, and the front will have the basic information (ie name, title, business, phone, email, website, etc..)

Target Market(s)

The target market are people into metaphysics, holistic healing, ancient Egyptian culture, aromatherapy, occult science, and the esoteric.

Industry/Entity Type

Business

Contact Information for Business Card

Name: Marlonda T. Pruitt
Title: Owner
Business: VELMORIQUE
Phone: 917.302.4417
Website: www.Velmorique.net
Facebook, Instagram, and twitter icons

Font styles to use
Serif
Decorative

Requirements
Must have
• My logo, and website.
Nice to have
• Ancient Egyptian hieroglyphs, Elegant designs around the border, or encircling the logo.

```html
<!DOCTYPE html>
<html lang="en">
<head>
<meta charset="utf-8">
<title>Velmorique Business Card</title>
<link rel="stylesheet" href="https://fonts.googleapis.com/css2?family=Arimo:wght@400&display=swap">
<style>
  :root {
    --backdrop: #c8d0b7;
    --card-black: #080a0a;
    --gold: #c9a24a;
    --gold-soft: #b8923f;
    --relief-brown: #5a3a1c;
    --relief-dark: #2a1a0c;
  }
  * { margin: 0; padding: 0; box-sizing: border-box; }
  html, body {
    width: 1200px; height: 1200px; overflow: hidden;
    background: var(--backdrop);
    font-family: "Arimo", Arial, sans-serif;
  }
  .card {
    position: absolute; left: 182px; width: 840px; height: 480px;
    background: var(--card-black);
    box-shadow: -4px 6px 10px rgba(0,0,0,0.35);
    overflow: hidden;
  }
  .card--front { top: 98px; }
  .card--back { top: 633px; }

  .relief-art {
    position: absolute; inset: 0;
    background:
      radial-gradient(ellipse 70% 55% at 15% 45%, rgba(90,58,28,0.85), rgba(42,26,12,0.6) 55%, rgba(8,10,10,0) 85%),
      linear-gradient(90deg, var(--relief-brown) 0%, var(--relief-dark) 40%, var(--card-black) 75%);
  }
  .divider {
    position: absolute; left: 0; right: 0; top: 229px; height: 2px;
    background: var(--gold-soft);
  }
  .brand {
    position: absolute; color: var(--gold);
    font-family: "Arimo", Arial, sans-serif; letter-spacing: 4px;
    background: var(--card-black); padding: 4px 10px;
  }
  .card--front .brand {
    left: 72px; top: 213px; font-size: 24px;
    background: transparent; text-shadow: none;
  }
  .card--front .brand-box {
    position: absolute; left: 62px; top: 206px; width: 270px; height: 46px;
    background: rgba(20,14,8,0.85);
  }
  .card--back .brand {
    left: 0; right: 0; top: 220px; text-align: center; font-size: 26px;
    background: transparent;
  }

  .contact {
    position: absolute; left: 494px; top: 165px; color: var(--gold);
  }
  .contact__name { font-size: 22px; line-height: 1.2; }
  .contact__title { font-size: 18px; line-height: 1.3; }
  .contact__lines { margin-top: 36px; font-size: 19px; }
  .contact__line { display: flex; align-items: center; gap: 8px; height: 34px; }
  .contact__line svg { width: 14px; height: 16px; flex: none; }
  .social { display: flex; gap: 12px; margin-top: 14px; }
  .social span {
    width: 19px; height: 19px; border-radius: 2px; background: var(--gold-soft);
  }
</style>
</head>
<body>
  <section class="card card--front">
    <div class="relief-art" role="img" aria-label="Carved Egyptian hieroglyph relief in warm brown tones fading into black"></div>
    <div class="divider"></div>
    <div class="brand-box"></div>
    <div class="brand">VELMORIQUE</div>
    <div class="contact">
      <div class="contact__name">Marlonda T. Pruitt</div>
      <div class="contact__title">Owner</div>
      <div class="contact__lines">
        <div class="contact__line">
          <svg viewBox="0 0 14 16"><path d="M3 2 Q8 8 3 14 L5 15 Q10 8 5 1 Z" fill="var(--gold)"/></svg>
          <span>917.302.4417</span>
        </div>
        <div class="contact__line">
          <svg viewBox="0 0 16 16"><circle cx="8" cy="8" r="7" fill="none" stroke="var(--gold)" stroke-width="1.6"/><path d="M1 8 H15 M8 1 Q4 8 8 15 M8 1 Q12 8 8 15" fill="none" stroke="var(--gold)" stroke-width="1"/></svg>
          <span>www.Velmorique.net</span>
        </div>
      </div>
      <div class="social" aria-label="Social profiles">
        <span></span><span></span><span></span>
      </div>
    </div>
  </section>

  <section class="card card--back">
    <div class="brand">VELMORIQUE</div>
  </section>
</body>
</html>
```